Postcard bar mitzvah invitations

I'm looking for glossy postcards which which contain information for my son's bar mitzvah - the time and place of the service, that it will be followed by a luncheon, the time and place of the party, and how to RSVP.

```html
<!DOCTYPE html>
<html lang="en">
<head>
<meta charset="utf-8">
<title>Bar Mitzvah Invitation – Jacob Marlow</title>
<link rel="stylesheet" href="https://fonts.googleapis.com/css2?family=Nunito+Sans:wght@400;700;800&display=swap">
<style>
  :root {
    --page-bg: #ececec;
    --card-bg: #ffffff;
    --ink: #3a3a3a;
    --shadow: rgba(0, 0, 0, 0.55);
    --gold-light: #f2cc3a;
    --gold-mid: #d9a935;
    --gold-deep: #c8952f;
  }
  * { margin: 0; padding: 0; box-sizing: border-box; }
  html, body {
    width: 1200px; height: 1000px; overflow: hidden;
    background: var(--page-bg);
    font-family: "Nunito Sans", "Avenir Next", Arial, sans-serif;
    color: var(--ink);
  }
  .invitation {
    position: absolute; left: 290px; top: 100px;
    width: 618px; height: 800px;
    background: var(--card-bg);
    text-align: center;
    box-shadow: 10px 10px 10px var(--shadow);
  }
  .invitation p { position: absolute; left: 0; width: 100%; white-space: nowrap; }
  .emblem {
    position: absolute; left: 244px; top: 72px;
    width: 118px; height: 134px;
    border-radius: 6px;
    background: linear-gradient(135deg, var(--gold-deep), var(--gold-light) 60%, var(--gold-mid));
    opacity: 0.85;
  }
  .intro { top: 216px; font-size: 15.5px; }
  .honoree {
    top: 250px; font-size: 43px; font-weight: 800; line-height: 1.15;
    background: linear-gradient(180deg, var(--gold-light), var(--gold-deep));
    -webkit-background-clip: text; background-clip: text; color: transparent;
  }
  .parents { top: 304px; font-size: 17px; }
  .service-date { top: 350px; font-size: 17px; font-weight: 700; }
  .service-venue { top: 379px; font-size: 17px; }
  .service-address { top: 408px; font-size: 18px; }
  .rsvp-deadline { top: 462px; font-size: 17px; font-weight: 800; }
  .rsvp-line {
    top: 490px; font-size: 22px; font-weight: 800;
    display: flex; justify-content: center; align-items: center; gap: 6px;
  }
  .rsvp-line.email { top: 527px; }
  .rsvp-line svg { width: 30px; height: 30px; }
  .luncheon { top: 591px; font-size: 17.5px; }
  .party-time { top: 644px; font-size: 20px; }
  .party-venue { top: 673px; font-size: 20px; }
  .party-address { top: 703px; font-size: 20px; }
</style>
</head>
<body>
  <main class="invitation">
    <div class="emblem" role="img" aria-label="Gold interlaced Star of David emblem"></div>

    <p class="intro">WE PRIDE AND JOY WE INVITE YOU TO JOIN US AS OUR SON</p>
    <p class="honoree">JACOB MARLOW</p>
    <p class="parents">PARENTS: HELEN &nbsp;AND MARK MARLOW</p>

    <p class="service-date">JUNE 13th, 2015 10:30 am</p>
    <p class="service-venue">TEMPLE BETH SHALOM</p>
    <p class="service-address">2810 CEDAR HILL ROAD, MAPLE GROVE, OHIO 44031</p>

    <p class="rsvp-deadline">RVSP BY MAY 31st</p>
    <p class="rsvp-line phone">
      <svg viewBox="0 0 30 30" aria-hidden="true">
        <path fill="var(--gold-mid)" d="M8 3c2 0 3 4 4 7 .4 1.3-2 2.2-2 3.2 0 2 3 6.5 5 7 1 .3 2-2 3.3-1.6 3 1 6.2 2.4 6.2 4.4 0 2-3 5-5.5 5C10 28 2 18 2 9.5 2 6.5 5.5 3 8 3z"/>
      </svg>
      216-555-0142
    </p>
    <p class="rsvp-line email">
      <svg viewBox="0 0 30 30" aria-hidden="true">
        <rect x="1" y="7" width="28" height="19" fill="var(--gold-mid)"/>
        <path d="M1 7 L15 18 L29 7" fill="none" stroke="#fff" stroke-width="1.5"/>
        <path d="M1 26 L12 16 M29 26 L18 16" stroke="#fff" stroke-width="1.2"/>
      </svg>
      marlow18@mailbox.com
    </p>

    <p class="luncheon">LIGHT LUNCH FOLLOWING BAR MITZVAH</p>

    <p class="party-time">4:00 pm to 8:00 pm</p>
    <p class="party-venue">Celebration continues at Jump 'n' Play</p>
    <p class="party-address">742 Ridgeview Road, Brookfield, Ohio 44067</p>
  </main>
</body>
</html>
```